Template for a Holiday Look Book

We need a holiday lookbook that we can use at a few different golf and country clubs. I am hoping we can get a design nailed down, that they would then be able to tweak and alter from club to club. We have Marketing Directors at each Club, but no one has the time to make this from scratch, but could tweak it much easier once the template is created. I have attached a word document with ideas and have a google file we have started for pictures as well.

Target Market(s)

counrty club members

Industry/Entity Type

Country Club

Font styles to use
Sans Serif

Colors
0355a3
ffffff
eaf1f7

Requirements
Must have
• holiday look and feel....enticing the items that would be purchased

```html
<!DOCTYPE html>
<html lang="en">
<head>
<meta charset="utf-8">
<title>Holiday Look Book – Opening Spread</title>
<link href="https://fonts.googleapis.com/css2?family=Crimson+Text:ital,wght@0,400;0,600;1,400&family=Montserrat:wght@400;600&display=swap" rel="stylesheet">
<style>
  :root{
    --club-blue:#0355a3;
    --club-navy:#1d3c6e;
    --ice:#eaf1f7;
    --white:#ffffff;
    --teal:#2fb0bf;
    --teal-soft:#7fcfd6;
    --stripe-mid:#5b8fc7;
    --stripe-light:#a9c6e4;
    --backdrop:#e4e7ea;
    --photo-warm:#b99a86;
    --photo-cool:#5d7f88;
  }
  *{margin:0;padding:0;box-sizing:border-box;}
  html,body{width:1200px;height:901px;overflow:hidden;background:var(--backdrop);}
  .spread{
    position:absolute;left:60px;top:250px;width:1080px;height:400px;
    display:flex;box-shadow:0 10px 30px rgba(0,0,0,.15);
  }
  .page{position:relative;width:540px;height:400px;background:var(--white);overflow:hidden;}
  .page--left{border-right:1px solid #d6dbe0;}
  .page svg.decor{position:absolute;inset:0;width:100%;height:100%;}
  .club-name{
    position:absolute;font-family:"Crimson Text",serif;font-style:italic;
    font-size:15px;color:var(--club-navy);display:flex;align-items:center;gap:6px;
    white-space:nowrap;
  }
  .club-name .mark{width:10px;height:10px;background:var(--club-navy);}
  .page--left .club-name{left:22px;top:70px;}
  .page--right .club-name{right:30px;top:22px;}
  .photo{
    position:absolute;left:120px;top:58px;width:420px;height:240px;
    background:linear-gradient(100deg,var(--photo-warm) 0%,#d8c5b6 45%,var(--photo-cool) 100%);
  }
  .greeting{
    position:absolute;right:150px;top:232px;width:400px;text-align:right;
    font-family:"Crimson Text",serif;font-size:15px;line-height:19px;color:var(--club-navy);
  }
  .greeting__line{
    display:inline-block;white-space:nowrap;padding:0 3px;
    background:rgba(255,255,255,.88);
  }
  .wish-tag{
    position:absolute;left:72px;top:70px;padding:2px 8px;
    background:var(--club-navy);color:var(--white);
    font-family:"Montserrat",sans-serif;font-size:11px;letter-spacing:.5px;
  }
</style>
</head>
<body>
<div class="spread">
  <section class="page page--left">
    <svg class="decor" viewBox="0 0 540 400" aria-hidden="true">
      <line x1="120" y1="42" x2="540" y2="42" stroke="var(--club-navy)" stroke-width="1"/>
    </svg>
    <div class="photo" role="img" aria-label="Family in Santa hats sitting with their dog beside a decorated Christmas tree"></div>
    <svg class="decor" viewBox="0 0 540 400" aria-hidden="true">
      <polygon points="540,58 540,298 420,298" fill="var(--teal)" opacity=".45"/>
      <polygon points="500,58 540,58 540,150" fill="var(--teal)" opacity=".7"/>
      <polygon points="120,190 120,400 330,400" fill="var(--white)"/>
    </svg>
    <div class="club-name"><span class="mark"></span>Aspen Ridge</div>
    <p class="greeting">
      <span class="greeting__line">Happy Holidays from Aspen Ridge Country Club!</span><br>
      <span class="greeting__line">Inside you'll find our favorite gifts for every</span><br>
      <span class="greeting__line">age and every hobby on your list.</span><br>
      <span class="greeting__line">So, gather the family at your Club this holiday season,</span><br>
      <span class="greeting__line">share some eggnog, and prepare</span><br>
      <span class="greeting__line">yourself to sleigh the holidays.</span>
    </p>
  </section>
  <section class="page page--right">
    <svg class="decor" viewBox="0 0 540 400" aria-hidden="true">
      <polygon points="0,0 70,0 22,130 0,130" fill="var(--teal)"/>
      <line x1="70" y1="48" x2="430" y2="48" stroke="var(--club-navy)" stroke-width="1"/>
      <g stroke="var(--teal-soft)" stroke-width="1">
        <line x1="72" y1="110" x2="450" y2="110"/>
        <line x1="72" y1="134" x2="450" y2="134"/>
        <line x1="72" y1="158" x2="450" y2="158"/>
        <line x1="72" y1="182" x2="450" y2="182"/>
        <line x1="72" y1="206" x2="450" y2="206"/>
        <line x1="72" y1="230" x2="450" y2="230"/>
        <line x1="72" y1="254" x2="450" y2="254"/>
        <line x1="72" y1="278" x2="450" y2="278"/>
        <line x1="72" y1="302" x2="450" y2="302"/>
        <line x1="72" y1="326" x2="450" y2="326"/>
      </g>
      <rect x="472" y="60" width="8" height="340" fill="var(--stripe-light)"/>
      <rect x="483" y="60" width="6" height="340" fill="var(--club-blue)"/>
      <rect x="492" y="60" width="9" height="340" fill="var(--stripe-mid)"/>
      <rect x="504" y="60" width="5" height="340" fill="var(--stripe-light)"/>
      <rect x="512" y="60" width="8" height="340" fill="var(--club-blue)"/>
      <rect x="523" y="60" width="6" height="340" fill="var(--stripe-mid)"/>
      <rect x="532" y="60" width="8" height="340" fill="var(--stripe-light)"/>
    </svg>
    <div class="club-name"><span class="mark"></span>Aspen Ridge</div>
    <div class="wish-tag">WISH LIST</div>
  </section>
</div>
</body>
</html>
```